We are a Machine Engineering Company based in Singapore since 1978. We supply tools & machine accessories to Manufacturing Plants using CNC Machines.

We sell Drills / Taps / Reamers / Carbide & Ceramic Inserts / Arbors / Chucks / Vise / etc...

We need an E Christmas Card to send out to our customers Worldwide.
It should have our Company Logo.
It should also include Greetings for the New Year.

Target Market(s)

Manufacturers of Aero Space / Oil & Gas / Automotive / Medical Science / etc

Requirements
Must have
• Company Logo
• Link : www.tovalix.com.sg
Nice to have
• Modern Designs
Should not have
• Porn or Suggestive Pictures.

```html
<!DOCTYPE html>
<html lang="en">
<head>
<meta charset="utf-8">
<title>Season's Greetings – Tovalix Tools</title>
<link href="https://fonts.googleapis.com/css2?family=Great+Vibes&display=swap" rel="stylesheet">
<style>
  :root {
    --red-deep: #8a0b22;
    --red-mid: #b3102f;
    --red-glow: #d21a48;
    --pink-band: #cf5a78;
    --pink-soft: #e3b1bf;
    --pink-pale: #efd3da;
    --white: #ffffff;
    --maroon: #8c1637;
  }
  html, body {
    margin: 0;
    padding: 0;
    overflow: hidden;
    background: var(--red-deep);
  }
  .card {
    position: relative;
    width: 1200px;
    height: 1194px;
    overflow: hidden;
    background: radial-gradient(ellipse 70% 60% at 55% 40%, var(--red-glow) 0%, var(--red-mid) 55%, var(--red-deep) 100%);
    font-family: 'Great Vibes', cursive;
  }
  .card__art {
    position: absolute;
    inset: 0;
    width: 1200px;
    height: 1194px;
  }
  .greeting {
    font-family: 'Great Vibes', cursive;
    fill: var(--white);
    font-weight: 400;
  }
  .brand {
    position: absolute;
    left: 18px;
    top: 1068px;
    display: flex;
    flex-direction: column;
    gap: 6px;
  }
  .brand__row {
    display: flex;
    align-items: center;
    gap: 10px;
  }
  .brand__dot {
    width: 40px;
    height: 40px;
    border-radius: 50%;
    background: var(--maroon);
  }
  .brand__name {
    font-family: 'Great Vibes', cursive;
    font-size: 46px;
    color: var(--maroon);
    line-height: 1;
  }
  .brand__link {
    font-family: 'Great Vibes', cursive;
    font-size: 28px;
    color: var(--maroon);
    line-height: 1;
    text-decoration: none;
    padding-left: 4px;
  }
</style>
</head>
<body>
<main class="card">
  <svg class="card__art" viewBox="0 0 1200 1194" xmlns="http://www.w3.org/2000/svg">
    <defs>
      <radialGradient id="tree-glow" cx="50%" cy="60%" r="60%">
        <stop offset="0%" stop-color="#ffffff" stop-opacity="0.75"/>
        <stop offset="60%" stop-color="#f6d4dc" stop-opacity="0.55"/>
        <stop offset="100%" stop-color="#e38aa0" stop-opacity="0.25"/>
      </radialGradient>
      <linearGradient id="band-fade" x1="0" y1="0" x2="0" y2="1">
        <stop offset="0%" stop-color="#d86a86"/>
        <stop offset="100%" stop-color="#c0506e"/>
      </linearGradient>
    </defs>

    <polygon class="tree" role="img" aria-label="Christmas tree formed from white snowflakes and stars"
             points="310,150 560,790 70,790" fill="url(#tree-glow)"/>

    <path class="wave wave--band" d="M0,830 C250,790 480,870 760,905 C980,930 1100,880 1200,840 L1200,1194 L0,1194 Z" fill="url(#band-fade)"/>
    <path class="wave wave--mid" d="M0,930 C280,890 560,960 860,1000 C1030,1020 1140,990 1200,960 L1200,1194 L0,1194 Z" fill="var(--pink-soft)" opacity="0.85"/>
    <path class="wave wave--low" d="M0,1040 C300,990 620,1060 920,1110 C1060,1130 1160,1110 1200,1095 L1200,1194 L0,1194 Z" fill="var(--pink-pale)" opacity="0.7"/>

    <g class="wave-lines" fill="none" stroke="var(--white)" stroke-linecap="round">
      <path d="M0,818 C240,770 480,860 760,895 C980,920 1100,870 1200,825" stroke-width="10" opacity="0.95"/>
      <path d="M0,850 C260,800 500,890 780,925 C990,945 1110,895 1200,860" stroke-width="4" opacity="0.7"/>
      <path d="M0,915 C280,870 560,945 860,985 C1030,1005 1140,975 1200,945" stroke-width="6" opacity="0.8"/>
      <path d="M0,1020 C300,975 620,1045 920,1095 C1060,1115 1160,1095 1200,1080" stroke-width="5" opacity="0.6"/>
    </g>

    <text class="greeting greeting--christmas" x="472" y="262" font-size="128"
          textLength="690" lengthAdjust="spacingAndGlyphs">Merry Christmas</text>
    <text class="greeting greeting--and" x="750" y="410" font-size="72"
          textLength="105" lengthAdjust="spacingAndGlyphs">and</text>
    <text class="greeting greeting--new-year" x="540" y="518" font-size="100"
          textLength="555" lengthAdjust="spacingAndGlyphs">Happy New Year</text>
  </svg>

  <div class="brand">
    <div class="brand__row">
      <span class="brand__dot"></span>
      <span class="brand__name">Tovalix Tools</span>
    </div>
    <a class="brand__link" href="http://www.tovalix.com.sg">www.tovalix.com.sg</a>
  </div>
</main>
</body>
</html>
```